Business Card Design Project

We need a business card design for a relatively new company called Velmar Gear. We design paddle (an outdoor winter sport primarily played in the midwest and east coast) and tennis bags for women and men. Velmar Gear is a lifestyle brand for the next generation country club goers. Our bags merge fashion with functionality and are making country club sports trendier and more fashionable.

I would like to include space for
Name: (will fill this in for employees)
Velmar Gear
Phone: (will do this)
Email:
www.velmargear.example

Would also like to include Chatterbook and Flitter icons.
Please do not use pictures of the bags - this is just to give you an idea of what style bags we sell.

Target Market(s)

30 to 40 year old men and women - luxury market

Industry/Entity Type

Fashion

Requirements
Must have
• Would like the company logo included

```html
<!DOCTYPE html>
<html lang="en">
<head>
<meta charset="utf-8">
<title>Velmar Gear — Business Card</title>
<link rel="stylesheet" href="https://fonts.googleapis.com/css2?family=Josefin+Sans:wght@300&family=Pinyon+Script&display=swap">
<style>
  :root {
    --leather-deep: #3a0906;
    --leather-mid: #6e140c;
    --leather-warm: #8a1f12;
    --panel-black: #070909;
    --ink-white: #ffffff;
    --emblem-dark: #2a0705;
    --emblem-faint: #1f1a1a;
    --chatter-blue: #3b63b0;
    --flitter-cyan: #4cc6d6;
  }
  * { margin: 0; padding: 0; box-sizing: border-box; }
  html, body { width: 1200px; height: 1042px; overflow: hidden; background: var(--panel-black); }
  .card-spread { position: relative; width: 1200px; height: 1042px; display: flex; }

  .card-back {
    position: relative; width: 600px; height: 1042px;
    background:
      radial-gradient(ellipse at 55% 50%, var(--leather-warm) 0%, var(--leather-mid) 45%, var(--leather-deep) 100%);
  }
  .back-emblem {
    position: absolute; left: 0; right: 0; top: 470px;
    text-align: center;
    font-family: "Josefin Sans", sans-serif; font-weight: 300;
    font-size: 68px; color: var(--emblem-dark);
  }
  .card-front {
    position: relative; width: 600px; height: 1042px;
    background: var(--panel-black); color: var(--ink-white);
    text-align: center;
  }
  .brand-header {
    position: absolute; left: 0; right: 0; top: 36px;
    display: flex; justify-content: center; align-items: center; gap: 18px;
    font-family: "Josefin Sans", sans-serif; font-weight: 300; font-size: 60px;
  }
  .brand-dot { width: 40px; height: 40px; border-radius: 50%; background: var(--ink-white); }
  .front-watermark {
    position: absolute; left: 0; right: 0; top: 300px;
    font-family: "Josefin Sans", sans-serif; font-weight: 300;
    font-size: 64px; color: var(--emblem-faint);
  }
  .contact { position: absolute; left: 0; right: 0; top: 548px; font-family: "Pinyon Script", cursive; }
  .contact-name { font-size: 54px; line-height: 66px; }
  .contact-company { font-size: 36px; line-height: 56px; }
  .contact-phone { font-size: 34px; line-height: 64px; }
  .contact-email { font-size: 34px; line-height: 56px; }
  .social {
    position: absolute; left: 0; right: 0; top: 828px;
    display: flex; justify-content: center; gap: 26px;
    font-family: "Josefin Sans", sans-serif; font-weight: 300; font-size: 20px;
  }
  .social-item { display: flex; align-items: center; gap: 8px; }
  .social-square { width: 22px; height: 22px; border-radius: 4px; }
  .social-square.chatter { background: var(--chatter-blue); }
  .social-square.flitter { background: var(--flitter-cyan); }
  .site-url {
    position: absolute; left: 0; right: 0; top: 985px;
    font-family: "Pinyon Script", cursive; font-size: 30px; color: var(--ink-white);
    text-align: center;
  }
</style>
</head>
<body>
<main class="card-spread">
  <section class="card-back" role="img" aria-label="Red leather texture background with the Velmar Gear mark">
    <div class="back-emblem">Velmar Gear</div>
    <p class="site-url">www.velmargear.example</p>
  </section>

  <section class="card-front">
    <header class="brand-header">
      <span class="brand-dot"></span>
      <span class="brand-name">Velmar Gear</span>
    </header>
    <div class="front-watermark" aria-hidden="true">Velmar Gear</div>
    <div class="contact">
      <p class="contact-name">Your Name</p>
      <p class="contact-company">Velmar Gear</p>
      <p class="contact-phone">+012345678912345</p>
      <p class="contact-email">Youremail@mailbox.example</p>
    </div>
    <nav class="social">
      <span class="social-item"><span class="social-square chatter"></span>Chatterbook</span>
      <span class="social-item"><span class="social-square flitter"></span>Flitter</span>
    </nav>
    <p class="site-url">www.velmargear.example</p>
  </section>
</main>
</body>
</html>
```